Wine Label for a Prosecco Wine Called Tavi

Prosecco is a white sparkling wine from Italy. We are looking for an eye catching, elegant label for this prosecco that is called "Tavi" because it is a young, fresh, lively white sparkling wine. (We do not want to see children or babies featured on the label-- just the name TAVI please.) Attached is the old label for your reference, and the bottle type that will be used , which is a dark green Burgundy style bottle (pls ignore the label on the bottle). Please no grapes or wine glasses on the label. We are looking for something: eye catching / fun / ELEGANT (not cheap). We would be happy with a fun color too. Remember-- elegant, eye catching! Thanks!
Updates

Hi All, I think I made a mistake in my brief and have updated it. I also uploaded a competitor's label that we like very much to give better direction to what we are looking for. Also, the word Tavi cannot be vertical, nor can it be broken. It needs to read: TAVI or Tavi. Thanks

Target Market(s)

American adults male and female.

Colors
abd036
33a6d7
33b8a4
ffcf3e

Requirements
Must have
• The mandatory information as shown on old labels. The word TAVI should be very prominent.
Nice to have
• The uploaded photo of a competitor's prosecco shows a label we really like... if you could play around with this shape and style we'd be very happy.
Should not have
• No grape images, no wine glass images, no images of babies or children.

```html
<!DOCTYPE html>
<html lang="it">
<head>
<meta charset="utf-8">
<title>Tavi Prosecco – Label</title>
<link href="https://fonts.googleapis.com/css2?family=Montserrat:wght@300;400&display=swap" rel="stylesheet">
<style>
  :root {
    --label-yellow: #ffcd36;
    --ink: #1f1c1a;
    --paper: #ffffff;
  }
  * { margin: 0; padding: 0; box-sizing: border-box; }
  html, body {
    width: 1200px;
    height: 1000px;
    overflow: hidden;
    background: var(--paper);
  }
  .canvas {
    position: relative;
    width: 1200px;
    height: 1000px;
  }
  .label {
    position: absolute;
    left: 338px;
    top: 60px;
    width: 524px;
    height: 880px;
    background: var(--label-yellow);
    color: var(--ink);
    font-family: "Montserrat", sans-serif;
    font-weight: 300;
    text-align: center;
    overflow: hidden;
  }
  .brand-mark {
    position: absolute;
    left: 0;
    top: 0;
    width: 100%;
    height: 496px;
    display: flex;
    align-items: center;
    justify-content: center;
    gap: 28px;
  }
  .brand-mark__square {
    width: 44px;
    height: 44px;
    background: var(--ink);
  }
  .brand-mark__name {
    font-size: 128px;
    font-weight: 300;
    letter-spacing: 6px;
    line-height: 1;
    color: var(--ink);
  }
  .wine-name {
    position: absolute;
    top: 528px;
    left: 0;
    width: 100%;
    font-size: 98px;
    font-weight: 300;
    letter-spacing: 3px;
    line-height: 1;
  }
  .wine-type {
    position: absolute;
    top: 636px;
    left: 0;
    width: 100%;
    font-size: 34px;
    font-weight: 300;
    letter-spacing: 1px;
    line-height: 1;
  }
  .region {
    position: absolute;
    top: 700px;
    left: 50%;
    transform: translateX(-50%);
    width: 196px;
    height: 58px;
    background: var(--ink);
    color: var(--label-yellow);
    font-size: 34px;
    font-weight: 300;
    letter-spacing: 1px;
    line-height: 58px;
  }
  .designation {
    position: absolute;
    top: 786px;
    left: 0;
    width: 100%;
    font-size: 24px;
    font-weight: 400;
    line-height: 1.1;
    letter-spacing: 0.3px;
  }
</style>
</head>
<body>
  <main class="canvas">
    <section class="label">
      <div class="brand-mark">
        <span class="brand-mark__square"></span>
        <span class="brand-mark__name">TAVI</span>
      </div>
      <h1 class="wine-name">TAVI</h1>
      <p class="wine-type">PROSECCO</p>
      <p class="region">VENETO</p>
      <p class="designation">FRIZZANTE<br>INDICAZIONE GEOGRICA TIPICA</p>
    </section>
  </main>
</body>
</html>
```